Webdesign

We are value investment firm in Denver, Colorado. We are a small but a very unique firm. We are looking for a minimalistic and clean design. We are competing against competitors that usually larger than we are, but we need to have a design that is better than theirs. Our clients put a tremendous trust in us when they let us manage their life savings. This website has to communicate trust but without traditional cliches (dollar bills, glasses, Harbor Ledger Gazette).
We had a coder/designer create our current website a few weeks ago http://brightkestrel.example/tolvan , we are not thrilled about the design. We are attaching our company's presentation, we'd like the design to be closer to the colors of that presentation.
We are looking for both design and coding (wordpress).
Updates
we will pay additional $200 for wordpress implementation
A few points of clarifications about design:
- don't use pictures of strangers
- we are a Denver/Colorado firm, if you use pictures use Denver/Colorado pictures
- full width website is probably what we are looking
- maybe parallax type of design
This theme http://quillframe.example/WP/Nimbra/ is how we see the new design
Industry/Entity Type
Investment

```html
<!DOCTYPE html>
<html lang="en">
<head>
<meta charset="utf-8">
<title>Tolvan — Private Portfolio Management</title>
<link href="https://fonts.googleapis.com/css2?family=Open+Sans:wght@400;600&family=Tinos:wght@400;700&display=swap" rel="stylesheet">
<style>
  :root {
    --navy: #1b2360;
    --text: #555555;
    --muted: #8a8a8a;
    --light: #a9a9a9;
    --rule: #e2e2e2;
    --panel: #ececec;
    --footer: #f2f2f2;
    --white: #ffffff;
  }
  * { box-sizing: border-box; margin: 0; padding: 0; }
  html, body { width: 1200px; height: 1000px; overflow: hidden; background: var(--white); }
  body { position: relative; font-family: "Open Sans", "Segoe UI", sans-serif; color: var(--text); }

  .brand { position: absolute; left: 287px; top: 38px; display: flex; align-items: center; gap: 8px; }
  .brand-mark { width: 10px; height: 10px; background: var(--navy); }
  .brand-name { font-family: "Tinos", serif; font-weight: 700; font-size: 24px; letter-spacing: 1px; color: var(--navy); line-height: 1; }

  .main-nav { position: absolute; top: 0; left: 0; font-family: "Tinos", serif; font-size: 8.5px; letter-spacing: .2px; }
  .main-nav a { position: absolute; top: 52px; color: var(--muted); text-decoration: none; white-space: nowrap; }
  .main-nav a.is-active { color: var(--navy); }
  .main-nav a.is-active::after { content: ""; position: absolute; left: 0; width: 43px; top: 24px; height: 2px; background: var(--navy); }
  .main-nav .divider { position: absolute; left: 915px; top: 52px; width: 1px; height: 10px; background: var(--light); }
  .main-nav svg { position: absolute; left: 926px; top: 53px; }

  .hero { position: absolute; left: 287px; top: 104px; width: 648px; height: 314px;
    background: linear-gradient(120deg, #3a3a3a 0%, #8d8d8d 30%, #dcdcdc 55%, #e9eef3 70%, #c9d9e8 85%, #2d8fd8 100%); }
  .hero-dots { position: absolute; left: 869px; top: 433px; display: flex; gap: 7px; }
  .hero-dots span { width: 7px; height: 7px; background: #c4c4c4; }
  .hero-dots span.is-current { background: var(--navy); }
  .hero-rule { position: absolute; left: 287px; top: 452px; width: 648px; height: 1px; background: var(--rule); }

  .tagline { position: absolute; left: 298px; top: 475px; width: 648px; text-align: center; font-family: "Tinos", serif; font-size: 13px; line-height: 17px; color: var(--light); }

  .features { position: absolute; left: 287px; top: 530px; width: 648px; height: 188px; background: var(--panel); }
  .feature { position: absolute; top: 28px; width: 136px; }
  .feature h2 { width: 130px; font-weight: 400; font-size: 15px; color: var(--text); white-space: nowrap; padding-bottom: 12px; border-bottom: 1px dotted #c9c9c9; }
  .feature p { margin-top: 11px; font-size: 8.2px; line-height: 12px; color: var(--muted); height: 48px; }
  .read-more { position: absolute; top: 112px; left: 0; display: flex; align-items: center; width: 71px; height: 16px; border-radius: 8px; background: #dedede; font-size: 7px; color: var(--muted); text-transform: uppercase; }
  .read-more svg { margin: 0 6px 0 1px; }

  .column-title { position: absolute; top: 748px; font-weight: 400; font-size: 16px; color: var(--text); }
  .articles { position: absolute; left: 287px; top: 781px; width: 201px; list-style: none; }
  .articles li { display: flex; height: 42px; border-bottom: 1px solid var(--rule); padding-top: 1px; }
  .articles li:last-child { border-bottom: none; }
  .articles time { flex: 0 0 31px; font-size: 12px; font-weight: 600; color: var(--muted); line-height: 13px; }
  .articles time small { display: block; font-size: 6.5px; font-weight: 400; }
  .articles a { width: 172px; font-size: 8px; line-height: 12px; color: var(--muted); text-decoration: none; }
  .all-articles { position: absolute; left: 287px; top: 914px; font-size: 6.5px; color: var(--muted); }

  .thumb { position: absolute; top: 784px; width: 175px; height: 85px; }
  .thumb-finance { left: 544px; background: linear-gradient(100deg, #4a4a4a 0%, #9a9a9a 40%, #ececec 75%, #d6d6d6 100%); }
  .thumb-watch { left: 760px; background: radial-gradient(circle at 60% 55%, #bdbdbd 0%, #8a8a8a 45%, #d9d9d9 100%); }
  .thumb-caption { position: absolute; top: 878px; width: 175px; font-size: 8.3px; line-height: 12px; color: var(--light); }

  .site-footer { position: absolute; left: 0; top: 957px; width: 1200px; height: 43px; background: var(--footer); font-size: 7px; color: var(--muted); }
  .site-footer .legal { position: absolute; left: 287px; top: 22px; }
  .site-footer .footer-nav { position: absolute; right: 265px; top: 22px; word-spacing: -1px; }
</style>
</head>
<body>
  <header>
    <div class="brand"><span class="brand-mark"></span><span class="brand-name">TOLVAN</span></div>
    <nav class="main-nav">
      <a href="#" class="is-active" style="left:559px">ABOUT US</a>
      <a href="#" style="left:625px">INVEST DIFRENTLY</a>
      <a href="#" style="left:729px">CONTENT</a>
      <a href="#" style="left:793px">CAREER</a>
      <a href="#" style="left:851px">CONTACT US</a>
      <span class="divider"></span>
      <svg width="10" height="10" viewBox="0 0 10 10" aria-label="Search"><circle cx="4" cy="4" r="3" fill="none" stroke="#a9a9a9" stroke-width="1.2"/><line x1="6.2" y1="6.2" x2="9.5" y2="9.5" stroke="#a9a9a9" stroke-width="1.4"/></svg>
    </nav>
  </header>

  <div class="hero" role="img" aria-label="Advisors reviewing portfolio charts and a tablet at a desk"></div>
  <div class="hero-dots"><span class="is-current"></span><span></span><span></span><span></span></div>
  <div class="hero-rule"></div>

  <p class="tagline">A disciplined, process-driven, value investment firm that provides a private portfolio management service tailored to individual and institutional clients tired of in-the-box, cookie-cutter, buy-and-hope investment products.</p>

  <section class="features">
    <article class="feature" style="left:21px">
      <h2>We Are Different</h2>
      <p>Our Active Value investment approach is crafted specifically for today's treacherous sideways mar-kets.</p>
      <a class="read-more"><svg width="14" height="14" viewBox="0 0 14 14"><circle cx="7" cy="7" r="6.5" fill="#fff" stroke="#ccc"/><path d="M5 5l2 2-2 2M7.5 5l2 2-2 2" fill="none" stroke="#999" stroke-width=".8"/></svg>Read more</a>
    </article>
    <article class="feature" style="left:180px">
      <h2>Investment Process</h2>
      <p>Our Active Value investment approach is crafted specifically for today's treacherous</p>
      <a class="read-more"><svg width="14" height="14" viewBox="0 0 14 14"><circle cx="7" cy="7" r="6.5" fill="#fff" stroke="#ccc"/><path d="M5 5l2 2-2 2M7.5 5l2 2-2 2" fill="none" stroke="#999" stroke-width=".8"/></svg>Read more</a>
    </article>
    <article class="feature" style="left:346px">
      <h2>Sideways Market</h2>
      <p>Our Active Value investment approach is crafted specifically for today's</p>
      <a class="read-more"><svg width="14" height="14" viewBox="0 0 14 14"><circle cx="7" cy="7" r="6.5" fill="#fff" stroke="#ccc"/><path d="M5 5l2 2-2 2M7.5 5l2 2-2 2" fill="none" stroke="#999" stroke-width=".8"/></svg>Read more</a>
    </article>
    <article class="feature" style="left:503px">
      <h2>We Build Model</h2>
      <p>Our Active Value investment approach is crafted specifically for today's treacherous sideways mar-kets.</p>
      <a class="read-more"><svg width="14" height="14" viewBox="0 0 14 14"><circle cx="7" cy="7" r="6.5" fill="#fff" stroke="#ccc"/><path d="M5 5l2 2-2 2M7.5 5l2 2-2 2" fill="none" stroke="#999" stroke-width=".8"/></svg>Read more</a>
    </article>
  </section>

  <h3 class="column-title" style="left:287px">Recent Articles</h3>
  <ul class="articles">
    <li><time>20<small>MAY</small></time><a href="#">The True Value of Macro Forecasting for Value Investors</a></li>
    <li><time>20<small>MAY</small></time><a href="#">The Modern Portfolio Theory Flat Earth Society</a></li>
    <li><time>20<small>MAY</small></time><a href="#">Crony Capitalism and the Sage of Silverton</a></li>
  </ul>
  <a class="all-articles">Continue to reading all articles ..</a>

  <h3 class="column-title" style="left:543px">Heading 2</h3>
  <div class="thumb thumb-finance" role="img" aria-label="Calculator and pen resting on financial charts"></div>
  <p class="thumb-caption" style="left:544px">Lorem Ipsum is simply dummy text of the printing and typesetting industry.</p>

  <h3 class="column-title" style="left:760px">Heading 3</h3>
  <div class="thumb thumb-watch" role="img" aria-label="Close-up of a pocket watch on printed pages"></div>
  <p class="thumb-caption" style="left:760px">Lorem Ipsum is simply dummy text of the printing and typesetting</p>

  <footer class="site-footer">
    <span class="legal">Copyright © 2014 Tolvan &nbsp;|&nbsp; PRIVACY POLICY</span>
    <span class="footer-nav">Home | About Us | Invest Difrently | Content | Career | Contact Us</span>
  </footer>
</body>
</html>
```